Professional business card design for Shelfwright Company
Biz card design utilizing existing Logo
Professional business card design for Shelfwright Company - Construction
Creative Brief
Use same font as used in my logo
Dean Halvik
President
not necessary
dean@brvmarrow.com
www.brvmarrow.com

```html
<!DOCTYPE html>
<html lang="en">
<head>
<meta charset="utf-8">
<title>Shelfwright Company – Business Card</title>
<link href="https://fonts.googleapis.com/css2?family=Oswald:wght@700&family=Open+Sans:wght@400;600&display=swap" rel="stylesheet">
<style>
  :root {
    --bg: #2a2430;
    --green-light: #8fbf3c;
    --green-mid: #6ea42c;
    --green-dark: #3f7a1c;
    --white: #ffffff;
    --ink: #1f1f1f;
    --soft-white: rgba(255,255,255,0.85);
  }
  * { box-sizing: border-box; margin: 0; padding: 0; }
  html, body {
    width: 1200px; height: 798px; overflow: hidden;
    background: var(--bg);
  }
  .canvas {
    width: 1200px; height: 798px;
    display: flex; align-items: center; justify-content: center; gap: 60px;
  }
  .card {
    position: relative; width: 500px; height: 286px;
    overflow: hidden; border-radius: 4px;
    box-shadow: 0 10px 30px rgba(0,0,0,0.35);
    font-family: "Open Sans", Arial, sans-serif;
  }
  .card--front { background: var(--white); }
  .card--back {
    background: radial-gradient(circle at 40% 45%, var(--green-light), var(--green-mid) 55%, var(--green-dark));
  }

  /* logo lockup */
  .logo { display: flex; align-items: center; gap: 12px; }
  .logo__mark { width: 34px; height: 34px; background: var(--green-mid); flex: none; }
  .logo__name {
    font-family: "Oswald", "Arial Narrow", sans-serif; font-weight: 700;
    color: var(--ink); text-transform: uppercase; line-height: 0.95;
    letter-spacing: 0.5px; white-space: nowrap;
  }

  /* front */
  .front__logo { position: absolute; left: 48px; top: 104px; }
  .front__logo .logo__name { font-size: 34px; }
  .front__arc {
    position: absolute; left: 300px; top: -187px;
    width: 660px; height: 660px; border-radius: 50%;
    background: radial-gradient(circle at 25% 50%, var(--green-light), var(--green-mid) 40%, var(--green-dark));
  }
  .front__web {
    position: absolute; right: 26px; bottom: 26px;
    display: flex; align-items: center; gap: 8px;
    color: var(--white); font-size: 12px;
  }

  /* back */
  .back__person { position: absolute; left: 36px; top: 40px; color: var(--white); }
  .back__name { font-size: 24px; font-weight: 600; }
  .back__title { font-size: 13px; color: var(--soft-white); margin-top: 2px; }
  .back__rule {
    position: absolute; left: 36px; top: 112px; width: 300px; height: 1px;
    background: rgba(255,255,255,0.6);
  }
  .back__contacts {
    position: absolute; left: 36px; top: 132px; list-style: none;
    color: var(--white); font-size: 12px;
  }
  .back__contacts li { display: flex; align-items: center; gap: 10px; margin-bottom: 12px; }
  .back__arc {
    position: absolute; left: 310px; top: 40px;
    width: 560px; height: 560px; border-radius: 50%;
    background: var(--white);
  }
  .back__logo { position: absolute; left: 350px; top: 204px; gap: 8px; }
  .back__logo .logo__mark { width: 20px; height: 20px; }
  .back__logo .logo__name { font-size: 18px; }

  .icon { width: 14px; height: 14px; flex: none; }
</style>
</head>
<body>
<main class="canvas">
  <section class="card card--front" aria-label="Card front">
    <div class="logo front__logo">
      <span class="logo__mark"></span>
      <span class="logo__name">Shelfwright<br>Company</span>
    </div>
    <div class="front__arc"></div>
    <div class="front__web">
      <svg class="icon" viewBox="0 0 16 16" fill="none" stroke="#fff" stroke-width="1.4"><circle cx="8" cy="8" r="6.5"/><path d="M1.5 8h13M8 1.5c2.2 2 2.2 11 0 13M8 1.5c-2.2 2-2.2 11 0 13"/></svg>
      <span>www.brvmarrow.com</span>
    </div>
  </section>

  <section class="card card--back" aria-label="Card back">
    <div class="back__person">
      <p class="back__name">Dean Halvik</p>
      <p class="back__title">President</p>
    </div>
    <div class="back__rule"></div>
    <ul class="back__contacts">
      <li>
        <svg class="icon" viewBox="0 0 16 16" fill="#fff"><path d="M4 1.5l2.3 3-1.4 1.6c.8 1.9 2.3 3.4 4.2 4.2l1.6-1.4 3 2.3-1.3 2.3C7 13 3 9 1.7 3.7z"/></svg>
        <span>012 345 6789</span>
      </li>
      <li>
        <svg class="icon" viewBox="0 0 16 16" fill="none" stroke="#fff" stroke-width="1.4"><rect x="1.5" y="3.5" width="13" height="9"/><path d="M1.5 3.5L8 9l6.5-5.5"/></svg>
        <span>dean@brvmarrow.com</span>
      </li>
      <li>
        <svg class="icon" viewBox="0 0 16 16" fill="none" stroke="#fff" stroke-width="1.4"><circle cx="8" cy="8" r="6.5"/><path d="M1.5 8h13M8 1.5c2.2 2 2.2 11 0 13M8 1.5c-2.2 2-2.2 11 0 13"/></svg>
        <span>www.brvmarrow.com</span>
      </li>
    </ul>
    <div class="back__arc"></div>
    <div class="logo back__logo">
      <span class="logo__mark"></span>
      <span class="logo__name">Shelfwright<br>Company</span>
    </div>
  </section>
</main>
</body>
</html>
```